Catering Menu Package

I currently have a complete menu package, which we have redesigned as far as content, now I need to it put together in a catalog type format. It is essentially 10-12 pages in length, and will be sent for print production. Upon receiving a final edit
Updates

I have added an example gif to the project.

I did this free hand this basically what I am looking for. please change text and type to whatever you think would look best. This is a total rough design so, feel free to change any and everything. The text for the page is on the word documents. If you need more images let me know I am in the process of getting as many images uploaded for your use.

Reason: I figured we got a late jump with questions, so i am extending a few days .

Target Market(s)

The target market is business who wish to have catered luncheons, breakfasts , meetings

Industry/Entity Type

Catering

Requirements
Must have
• I have attached a copy of the text that what we want in the package, our logo, and i have also attached a catering package of another company to give you an idea what the finished product will be
Should not have
• It should not look identical to the example catering packages, these are for some inspiration we want our own design with the same type of look and feel

```html
<!DOCTYPE html>
<html lang="en">
<head>
<meta charset="utf-8">
<title>Breakfast Catering Menu – Harbor Field Caterers</title>
<link rel="stylesheet" href="https://fonts.googleapis.com/css2?family=Lobster+Two:ital,wght@1,700&family=Sorts+Mill+Goudy:ital@0;1&display=swap">
<style>
  :root{
    --stage:#ece7df;
    --paper:#e6dccd;
    --orange:#f47a20;
    --green:#5db85a;
    --ink:#1d1a16;
    --white:#ffffff;
    --photo-light:#e9dcc2;
    --photo-dark:#b58a4e;
    --photo-green:#6f8c3c;
  }
  *{box-sizing:border-box;margin:0;padding:0}
  html,body{width:1200px;height:800px;overflow:hidden;background:var(--stage)}
  body{position:relative;font-family:"Sorts Mill Goudy",Georgia,serif;color:var(--ink)}
  .page{position:absolute;top:16px;width:566px;height:746px;background:var(--paper);overflow:hidden}
  .page--front{left:22px}
  .page--back{left:608px}
  .page-art{position:absolute;inset:0}
  .header-rule{position:absolute;left:0;top:30px;width:470px;height:5px;background:var(--orange)}
  .page-title{position:absolute;left:88px;top:12px;height:40px;padding:0 16px;background:var(--orange);color:var(--white);
    font-family:"Lobster Two",cursive;font-style:italic;font-weight:700;font-size:28px;line-height:40px;letter-spacing:.5px}
  .menu-item{position:absolute;left:0;width:450px;text-align:center}
  .menu-item h2{font-family:"Sorts Mill Goudy",Georgia,serif;font-style:italic;font-weight:400;color:var(--orange);font-size:25px;line-height:28px}
  .menu-item p{font-size:11.5px;line-height:17.5px;padding:0 30px}
  .menu-item .price{font-size:14px;margin-top:6px}
  .page--back .menu-item p{padding:0 22px}
  .notice{position:absolute;left:12px;top:656px;width:398px;height:28px;border-radius:8px;background:var(--green);
    color:var(--white);font-size:10px;line-height:13px;text-align:center;padding-top:1px}
  .contact-bar{position:absolute;left:0;top:688px;width:446px;height:58px;background:var(--orange);color:var(--white)}
  .contact-bar .call{position:absolute;left:20px;top:4px;font-size:10px;font-style:italic}
  .contact-bar .phone{position:absolute;left:32px;top:18px;display:flex;align-items:center;gap:8px;font-size:23px;font-style:italic;color:var(--ink)}
  .contact-bar .address{position:absolute;left:252px;top:6px;font-size:10px;line-height:13px}
  .brand{position:absolute;left:440px;top:519px;width:126px;height:227px;display:flex;flex-direction:column;align-items:center;justify-content:center;gap:12px}
  .brand .mark{width:64px;height:64px;border-radius:50%;background:var(--orange)}
  .brand .name{font-size:17px;line-height:20px;text-align:center;color:var(--ink)}
</style>
</head>
<body>

<section class="page page--front">
  <svg class="page-art" width="566" height="746" viewBox="0 0 566 746">
    <defs>
      <linearGradient id="bread" x1="0" y1="0" x2="1" y2="1">
        <stop offset="0" stop-color="var(--photo-light)"/>
        <stop offset=".6" stop-color="var(--photo-dark)"/>
        <stop offset="1" stop-color="#e8e6e2"/>
      </linearGradient>
    </defs>
    <path role="img" aria-label="Photo of sliced breakfast bread with cranberries on a plate" fill="url(#bread)"
          d="M470 0 H566 V520 H440 C452 420 442 320 440 230 C438 130 462 60 470 0 Z"/>
    <rect x="440" y="519" width="126" height="227" fill="var(--white)"/>
  </svg>
  <div class="header-rule"></div>
  <h1 class="page-title">Light Breakfast</h1>

  <article class="menu-item" style="top:66px">
    <h2>Quick and Easy</h2>
    <p>French Pastry, a Fresh Baked Gourmet Muffin,and<br>Whole Fresh Fruit(Featuring Local Apples<br>and Peaches, California Oranges, or Bananas).</p>
    <p class="price">$&amp;.&amp;&amp;</p>
  </article>
  <article class="menu-item" style="top:172px">
    <h2>Fast Farmhouse</h2>
    <p>Fresh baked Breakfast Bread and Buttery Biscuits,<br>Whipped Butter and House-made Strawberry Jam and<br>Local Fruit Jellies, and Whole Fresh Fruit(Featuring<br>Local Apples and Peaches, California Oranges, or Bananas).</p>
    <p class="price">$&amp;.&amp;&amp;</p>
  </article>
  <article class="menu-item" style="top:297px">
    <h2>Light and Lean</h2>
    <p>Individual Yogurt, Fresh Fruit and<br>Berry Cups and House-made Granola.</p>
    <p class="price">$&amp;.&amp;&amp;</p>
  </article>
  <article class="menu-item" style="top:390px">
    <h2>New Yorker</h2>
    <p>Brooklyn Bagel, Whipped Cream Cheese, House-made<br>Strawberry Jam and Local Fruit Jellies, Whipped Butter,<br>and Whole Fresh Fruit(Featuring Local Apples and Peaches,<br>California Oranges, or Bananas). Add Smoked Salmon</p>
    <p class="price">$&amp;.&amp;&amp;</p>
  </article>
  <article class="menu-item" style="top:518px">
    <h2>City Farmhouse</h2>
    <p>Fresh Baked Buttery Biscuits, Gourmet Muffins and<br>Breakfast Breads, Brooklyn Bagels, Whole Fresh<br>Fruit(Featuring Local Apples and Peaches, California<br>Oranges, or Bananas), Whipped Butter and Cream Cheese,<br>House-made Strawberry Jam and Local Fruit Jellies.</p>
    <p class="price" style="margin-top:2px">$&amp;.&amp;&amp;</p>
  </article>

  <p class="notice">All Prices are per Person, with a 10 person minimum order per item chosen.<br>Local Products used when available and in season</p>
  <footer class="contact-bar">
    <span class="call">CALL OR EMAIL US TODAY:</span>
    <span class="phone">
      <svg width="24" height="20" viewBox="0 0 24 20" aria-hidden="true"><path fill="var(--ink)" d="M2 6 C2 2 22 2 22 6 L22 8 L17 8 L17 5 L7 5 L7 8 L2 8 Z M6 9 H18 L21 18 H3 Z"/><circle cx="12" cy="13" r="2.5" fill="var(--orange)"/></svg>
      410-555-0182
    </span>
    <span class="address">218 Alder Lane<br>Millbrook, MD 20999<br>www.harborfieldcaterers.com</span>
  </footer>
  <div class="brand">
    <span class="mark"></span>
    <span class="name">Harbor Field<br>Caterers</span>
  </div>
</section>

<section class="page page--back">
  <svg class="page-art" width="566" height="746" viewBox="0 0 566 746">
    <defs>
      <linearGradient id="quiche" x1="0" y1="0" x2="1" y2="1">
        <stop offset="0" stop-color="#f1e3b8"/>
        <stop offset=".5" stop-color="#dcc07a"/>
        <stop offset=".8" stop-color="var(--photo-green)"/>
        <stop offset="1" stop-color="#e7d39a"/>
      </linearGradient>
    </defs>
    <path role="img" aria-label="Photo of a spinach quiche slice with flaky crust" fill="url(#quiche)"
          d="M440 0 H566 V520 H422 C432 420 430 320 428 230 C426 130 436 60 440 0 Z"/>
    <rect x="422" y="519" width="144" height="227" fill="var(--white)"/>
  </svg>
  <div class="header-rule"></div>
  <h1 class="page-title">Hearty Breakfast</h1>

  <article class="menu-item" style="top:66px">
    <h2>Breakfast Croissantwich</h2>
    <p>Farm-fresh Eggs and Cheese, Farm-fresh Eggs and Applewood<br>Smoked Bacon, Farm-Fresh Eggs and Maple Sausage, or Farm-Fresh<br>Eggs and Scrapple. Don't want a Croissant? Sandwich size English<br>Muffins, Fresh Baked Biscuits, and Brooklyn Bagels available on request.</p>
    <p class="price" style="margin-top:12px">$&amp;.&amp;&amp;</p>
  </article>
  <article class="menu-item" style="top:232px">
    <h2>Chef Marco's Breakfast Burrito</h2>
    <p>Jumbo flour tortilla filled with Redskin Potatoes, Farm-fresh Eggs,<br>Shredded Cheddar, and your choice of meat or extra cheese. Choose<br>from; Chorizo Sausage, Applewood Smoked Bacon, Maple Sausage, or<br>Country Ham. Served with fresh Chef made Salsa. &nbsp;&nbsp;&nbsp;&nbsp;&nbsp;Add avocado</p>
    <p class="price" style="margin-top:0">$&amp;.&amp;&amp;</p>
  </article>
  <article class="menu-item" style="top:385px">
    <h2>Individual Quiche</h2>
    <p>Spinach and Cheese, Local Tomato and Applewood Smoked Bacon,<br>Maple Sausage and Redskin Potato, or Asparagus and Crab.</p>
    <p class="price">$&amp;.&amp;&amp;</p>
  </article>
  <article class="menu-item" style="top:490px">
    <h2>Farmhouse Breakfast</h2>
    <p>Country Cheddar Scrambled Eggs Served with Redskin Potato<br>Hash Browns, Baked Spiced Apples, Fresh Baked Gourmet<br>Muffins and Buttery Biscuits, and Your Choice of One;<br>Applewood Smoked Bacon, Maple Sausage Links, or Country Ham.</p>
    <p class="price" style="margin-top:10px">$&amp;.&amp;&amp;</p>
  </article>

  <p class="notice">All Prices are per Person, with a 10 person minimum order per item chosen.<br>Local Products used when available and in season</p>
  <footer class="contact-bar" style="width:424px">
    <span class="call">CALL OR EMAIL US TODAY:</span>
    <span class="phone">
      <svg width="24" height="20" viewBox="0 0 24 20" aria-hidden="true"><path fill="var(--ink)" d="M2 6 C2 2 22 2 22 6 L22 8 L17 8 L17 5 L7 5 L7 8 L2 8 Z M6 9 H18 L21 18 H3 Z"/><circle cx="12" cy="13" r="2.5" fill="var(--orange)"/></svg>
      410-555-0182
    </span>
    <span class="address" style="left:238px">218 Alder Lane<br>Millbrook, MD 20999<br>www.harborfieldcaterers.com</span>
  </footer>
  <div class="brand" style="left:422px;width:144px">
    <span class="mark"></span>
    <span class="name">Harbor Field<br>Caterers</span>
  </div>
</section>

</body>
</html>
```